Marta Business Card

My wife is going to start her own business with renting holiday appartments to tourists. She needs a design for a new business card... and a new web site.
Look at Stayvolt "Erholung auf dem Lindenwäldchen"

Target Market(s)

Give business card to prospects at any situation

Contact Information for Business Card

not sure what this means

Font styles to use
Script

Colors
fec41a
fee18a

Requirements
Must have
• My wife's handwriting is difficult to read:
Entspannen - Loslassen - Auftanken
Marta & das Lindenwäldchen
Urlaub an einem besonderen Ort
Marta Brecke
Grauer Pfad 7
18471 Alt Feldow
post@marta-brecke.de
www.lindenwaeldchen.net
Nice to have
• Beige background
Font like handwriting

```html
<!DOCTYPE html>
<html lang="de">
<head>
<meta charset="utf-8">
<title>Marta Brecke – Visitenkarte</title>
<link href="https://fonts.googleapis.com/css2?family=Allura&family=Dancing+Script:wght@500&family=Montserrat:wght@400&display=swap" rel="stylesheet">
<style>
  :root {
    --card: #1d1d1b;
    --gold: #fec41a;
    --band: #fee18a;
    --ink: #1d1d1b;
    --paper: #ffffff;
    --text-light: #f4f4f2;
    --pattern: #262624;
  }
  * { margin: 0; padding: 0; box-sizing: border-box; }
  html, body {
    width: 1200px; height: 1001px; overflow: hidden;
    background: var(--paper);
  }
  .canvas { position: relative; width: 1200px; height: 1001px; }
  .card {
    position: absolute; left: 330px; width: 540px; height: 309px;
    background: var(--card); overflow: hidden;
  }
  .card--front { top: 147px; }
  .card--back { top: 570px; }

  /* Front */
  .front-ornament {
    position: absolute; left: 75px; top: 125px; width: 410px; height: 184px;
    background: radial-gradient(ellipse at 50% 45%, #2a2a28 0%, #232321 50%, rgba(29,29,27,0) 80%);
  }
  .brand-name {
    position: absolute; left: 0; right: 0; top: 108px;
    text-align: center;
    font-family: "Allura", cursive;
    font-size: 50px; font-weight: 400; line-height: 1;
    color: var(--gold);
  }
  .tagline {
    position: absolute; left: 0; right: 0; top: 228px;
    text-align: center;
    font-family: "Allura", cursive;
    font-size: 24px; line-height: 1;
    color: var(--gold);
  }

  /* Back */
  .back-ornament {
    position: absolute; left: 335px; top: 0; width: 205px; height: 309px;
    background: var(--pattern);
  }
  .person-name {
    position: absolute; left: 50px; top: 72px;
    font-family: "Dancing Script", cursive;
    font-size: 38px; font-weight: 500; line-height: 1;
    color: var(--gold);
  }
  .contact-list {
    position: absolute; left: 50px; top: 130px;
    list-style: none;
    font-family: "Montserrat", sans-serif;
    font-size: 14.5px; line-height: 18px;
    color: var(--text-light);
  }
  .contact-item { display: flex; align-items: flex-start; margin-bottom: 9px; }
  .contact-icon { width: 10px; height: 18px; margin-right: 4px; flex: none; }
  .contact-sep { color: var(--text-light); margin-right: 7px; opacity: .8; }
  .slogan-band {
    position: absolute; left: 0; top: 240px; width: 540px; height: 47px;
    background: var(--band);
    display: flex; align-items: center; justify-content: center;
  }
  .slogan {
    font-family: "Dancing Script", cursive;
    font-size: 30px; font-weight: 500; line-height: 1;
    color: var(--ink);
  }
</style>
</head>
<body>
<div class="canvas">

  <section class="card card--front">
    <div class="front-ornament" role="img" aria-label="Feine Blumen- und Blattornamentik im Hintergrund"></div>
    <h1 class="brand-name">Marta &amp; das Lindenwäldchen</h1>
    <p class="tagline">Entspannen ~ Loslassen ~ Auftanken</p>
  </section>

  <section class="card card--back">
    <div class="back-ornament" role="img" aria-label="Dezentes Mandala-Ornamentmuster"></div>
    <h2 class="person-name">Marta Brecke</h2>
    <ul class="contact-list">
      <li class="contact-item">
        <svg class="contact-icon" viewBox="0 0 10 18" aria-hidden="true"><path d="M5 4.5a3.2 3.2 0 0 1 3.2 3.2C8.2 10 5 13.5 5 13.5S1.8 10 1.8 7.7A3.2 3.2 0 0 1 5 4.5z" fill="none" stroke="#f4f4f2" stroke-width=".9"/><circle cx="5" cy="7.7" r="1.1" fill="none" stroke="#f4f4f2" stroke-width=".8"/></svg>
        <span class="contact-sep">|</span>
        <span>Grauer Pfad 7<br>18471 Alt Feldow</span>
      </li>
      <li class="contact-item">
        <svg class="contact-icon" viewBox="0 0 10 18" aria-hidden="true"><rect x=".8" y="7" width="8.4" height="6" fill="none" stroke="#f4f4f2" stroke-width=".8"/><path d="M.8 7 5 10.5 9.2 7M.8 13l3-3M9.2 13l-3-3" fill="none" stroke="#f4f4f2" stroke-width=".7"/></svg>
        <span class="contact-sep">|</span>
        <span>post@marta-brecke.de</span>
      </li>
      <li class="contact-item">
        <svg class="contact-icon" viewBox="0 0 10 18" aria-hidden="true"><circle cx="5" cy="10" r="3.8" fill="none" stroke="#f4f4f2" stroke-width=".8"/><ellipse cx="5" cy="10" rx="1.6" ry="3.8" fill="none" stroke="#f4f4f2" stroke-width=".7"/><path d="M1.2 10h7.6" stroke="#f4f4f2" stroke-width=".7"/></svg>
        <span class="contact-sep">|</span>
        <span>www.lindenwaeldchen.net</span>
      </li>
    </ul>
    <div class="slogan-band">
      <p class="slogan">Urlaub an einem besonderen Ort</p>
    </div>
  </section>

</div>
</body>
</html>
```